Brimvale Business Card

I need attractive business card desgnie that shows my contact information

,Logo and service that we provide and also QR and the font must be readable and designer must submit the design in editable PSD format and Jpg format .The artwork must meet the following printing specification

Artwork Specification
Full Bleed Size (starting document size)
Finished artwork should use the full bleed dimensions for best results
92 x 54 mm
1085 x 635 pixels
Document Trim Size (final size after being cut)
89 x 51 mm
1050 x 600 pixels
Resolution
300 DPI
Please be sure to keep all text within the safe margin.

List of Services

Medical Chart Scanning

EMR Technical Support

Hardware Installation

Document Management Solutions

Data Recovery

Data Backup

Cloud Computing Solutions

VOIP Solutions

Target Market(s)

Lawyers,Doctors ,Small Business

Industry/Entity Type

Printing

Requirements
Nice to have
• List Of the services
Medical Chart Scanning

EMR Technical Support

Hardware Installation

Data Recovery

Data Backup

Cloud Computing Solutions

VOIP Solutions

```html
<!DOCTYPE html>
<html lang="en">
<head>
<meta charset="utf-8">
<title>Brimvale Business Card</title>
<link href="https://fonts.googleapis.com/css2?family=Alegreya:ital,wght@1,400;1,500&family=Alegreya+Sans:wght@500&family=Alegreya+Sans+SC:wght@700&display=swap" rel="stylesheet">
<style>
  :root {
    --ink: #1e1e1e;
    --charcoal: #3a3a3a;
    --brand-red: #c0180c;
    --band-red: #d81e16;
    --band-red-light: #f0625c;
    --paper: #ffffff;
    --night: #0b0b0b;
    --code-frame: #2a2a2a;
  }
  html, body {
    margin: 0;
    padding: 0;
    width: 1200px;
    height: 704px;
    overflow: hidden;
    background: var(--paper);
  }
  .card {
    position: relative;
    width: 1200px;
    height: 704px;
    overflow: hidden;
    background: var(--paper);
    font-family: "Alegreya", Georgia, serif;
    font-style: italic;
    color: var(--ink);
  }
  .card-backdrop {
    position: absolute;
    inset: 0;
    width: 1200px;
    height: 704px;
  }
  .brand {
    position: absolute;
    left: 290px;
    top: 120px;
    display: flex;
    align-items: center;
    gap: 36px;
  }
  .brand-dot {
    width: 118px;
    height: 118px;
    border-radius: 50%;
    background: var(--brand-red);
  }
  .brand-name {
    font-family: "Alegreya Sans", Arial, sans-serif;
    font-style: normal;
    font-weight: 500;
    font-size: 160px;
    line-height: 1;
    color: var(--charcoal);
    letter-spacing: -1px;
  }
  .person {
    position: absolute;
    left: 733px;
    top: 300px;
  }
  .person-name {
    margin: 0;
    font-size: 50px;
    font-weight: 400;
    line-height: 1;
    color: var(--ink);
  }
  .person-name .surname { color: var(--brand-red); }
  .person-role {
    margin: 4px 0 0;
    font-size: 17px;
    letter-spacing: 4.3px;
    text-transform: uppercase;
    color: var(--ink);
  }
  .contact-list {
    list-style: none;
    margin: 18px 0 0;
    padding: 0;
    font-size: 25px;
    line-height: 33px;
  }
  .qr-code {
    position: absolute;
    left: 1050px;
    top: 408px;
    width: 104px;
    height: 104px;
    box-sizing: border-box;
    border: 8px solid var(--code-frame);
    background: var(--paper);
  }
  .services {
    position: absolute;
    left: 102px;
    top: 292px;
  }
  .services-title {
    margin: 0;
    font-size: 23px;
    font-weight: 400;
    line-height: 28px;
    color: var(--brand-red);
  }
  .services-list {
    list-style: none;
    margin: 0;
    padding: 0;
    font-size: 23px;
    line-height: 28px;
  }
  .company-line {
    position: absolute;
    left: 0;
    right: 0;
    top: 655px;
    text-align: center;
    font-family: "Alegreya Sans SC", Arial, sans-serif;
    font-weight: 700;
    font-style: normal;
    font-size: 21px;
    letter-spacing: 2.4px;
    color: var(--paper);
    word-spacing: 4px;
  }
  .company-line span { margin: 0 18px; }
</style>
</head>
<body>
<div class="card">
  <svg class="card-backdrop" viewBox="0 0 1200 704" aria-hidden="true">
    <defs>
      <linearGradient id="mist-fade" x1="0" y1="0" x2="0" y2="1">
        <stop offset="0" stop-color="#bdbdbd"/>
        <stop offset="1" stop-color="#ffffff" stop-opacity="0"/>
      </linearGradient>
      <linearGradient id="red-band" x1="0" y1="0" x2="0" y2="1">
        <stop offset="0" stop-color="#f0625c"/>
        <stop offset="0.35" stop-color="#d81e16"/>
        <stop offset="1" stop-color="#b50f0a"/>
      </linearGradient>
      <linearGradient id="grey-band" x1="0" y1="0" x2="0" y2="1">
        <stop offset="0" stop-color="#ffffff"/>
        <stop offset="1" stop-color="#d6d6d6"/>
      </linearGradient>
    </defs>
    <path class="top-shade" d="M0 0 H1200 V120 C1000 95 720 80 520 130 C380 165 220 250 70 260 L0 262 Z" fill="url(#mist-fade)"/>
    <path class="top-wave" d="M0 0 H1200 V82 C1080 65 880 60 700 70 C520 82 430 110 330 180 C260 228 170 250 95 238 C50 230 20 215 0 200 Z" fill="#0b0b0b"/>
    <path class="low-shade" d="M0 500 C200 520 420 570 620 575 C860 580 1040 530 1200 505 V704 H0 Z" fill="url(#grey-band)"/>
    <path class="bottom-wave" d="M0 552 C200 575 420 618 640 622 C860 626 1040 570 1200 548 V704 H0 Z" fill="url(#red-band)"/>
  </svg>

  <div class="brand">
    <div class="brand-dot"></div>
    <div class="brand-name">Brimvale</div>
  </div>

  <section class="services">
    <h2 class="services-title">Services Include:</h2>
    <ul class="services-list">
      <li>-Medical Chart Scanning</li>
      <li>-EMR Technical Support</li>
      <li>-Hardware Installation</li>
      <li>-Document Management Solutions</li>
      <li>-Data Recovery</li>
      <li>-Data Backup</li>
      <li>-Cloud Computing Solutions</li>
      <li>-VOIP Solutions</li>
    </ul>
  </section>

  <section class="person">
    <h1 class="person-name">Karim <span class="surname">Haddad</span></h1>
    <p class="person-role">Technical Support Specialist</p>
    <ul class="contact-list">
      <li>Ph: 306.555.0148 ext 2</li>
      <li>Cel: 306.555.0173</li>
      <li>Fax: 306.555.0149</li>
      <li>Em: karim@brimvale.com</li>
    </ul>
  </section>

  <div class="qr-code" role="img" aria-label="QR code linking to Brimvale contact details"></div>

  <footer class="company-line">
    <span>Brimvale Solutions</span><span>1187B Harlow St Elmridge ,SK S4R 2K7</span><span>Canada</span>
  </footer>
</div>
</body>
</html>
```